Property Report

8 page document, similar theme to our website (www.harbourandvale.example) and previous brochure (provided). All content provided. We want a professional looking document. We need ASAP. Thanks!

Industry/Entity Type

Property

Font styles to use
Serif
Sans Serif

Colors
ffc214
ffcf3e
fee18a
fff3d1

Requirements
Must have
• Page 1: Cover
Page 2: Content
Page 3: About Us
Page 4: Site Description
Page 5: Scheme
Page 6: Analysis
Page 7: Conclusion
Page 8: Contact Details

```html
<!DOCTYPE html>
<html lang="en">
<head>
<meta charset="utf-8">
<title>Contents Page</title>
<link href="https://fonts.googleapis.com/css2?family=Antonio:wght@400&family=Open+Sans:wght@700&display=swap" rel="stylesheet">
<style>
  :root {
    --brand-yellow: #fec41b;
    --slate: #4f5052;
    --white: #ffffff;
  }
  html, body {
    margin: 0;
    padding: 0;
    overflow: hidden;
  }
  .page {
    position: relative;
    width: 848px;
    height: 1200px;
    overflow: hidden;
    background: var(--slate);
  }
  .title-band {
    position: absolute;
    left: 0;
    top: 0;
    width: 848px;
    height: 477px;
    background: var(--brand-yellow);
  }
  .page-title {
    position: absolute;
    left: 0;
    width: 848px;
    top: 262px;
    margin: 0;
    text-align: center;
    font-family: "Antonio", "Oswald", sans-serif;
    font-weight: 400;
    font-size: 112px;
    line-height: 1;
    letter-spacing: 3px;
    color: var(--white);
  }
  .contents-list {
    position: absolute;
    left: 246px;
    top: 540px;
    margin: 0;
    padding: 0;
    list-style: none;
    font-family: "Open Sans", "Calibri", sans-serif;
    font-weight: 700;
    font-size: 30px;
    line-height: 1;
    letter-spacing: 1px;
  }
  .contents-item {
    height: 81.5px;
  }
  .item-page {
    color: var(--white);
  }
  .item-title {
    color: var(--brand-yellow);
  }
</style>
</head>
<body>
  <main class="page">
    <header class="title-band">
      <h1 class="page-title">Contents Page</h1>
    </header>
    <ul class="contents-list">
      <li class="contents-item"><span class="item-page">Page 3:</span> <span class="item-title">About Us</span></li>
      <li class="contents-item"><span class="item-page">Page 4:</span> <span class="item-title">Site Description</span></li>
      <li class="contents-item"><span class="item-page">Page 5:</span> <span class="item-title">Scheme</span></li>
      <li class="contents-item"><span class="item-page">Page 6:</span> <span class="item-title">Case Studies</span></li>
      <li class="contents-item"><span class="item-page">Page 7:</span> <span class="item-title">Analysis</span></li>
      <li class="contents-item"><span class="item-page">Page 8:</span> <span class="item-title">Conclusion</span></li>
      <li class="contents-item"><span class="item-page">Page 9:</span> <span class="item-title">Contact Details</span></li>
    </ul>
  </main>
</body>
</html>
```